Wordpress 6 pages GLAM design for hair salon

Hi guys.
I need a glam & easy to navigate web design for my (women only) new hair salon.
I have a logo. You can see in attached files.
I like 3d backgrounds.
My favourite colours choice: any variety of pink(hot & very soft), white, black, grey.
I would like to see website very feminine, glamorous & kind of old Hollywood and Doreen Valcourt inspired.
Of course it should have plug ins, like social media, map, security etc.
My website now: http://velorimtresses.example

Designs what I like:
http://quarnetsalon.example
http://lumbrivespastudio.example
http://www.tindrelgraphicdesign.example/boutique-graphic-web-folio.html

Target Market(s)

WOMEN

Industry/Entity Type

Boutique

Requirements
Should not have
• any cartoon or other characters!

```html
<!DOCTYPE html>
<html lang="en">
<head>
<meta charset="utf-8">
<title>Velorim Tresses Hair Designs</title>
<link href="https://fonts.googleapis.com/css2?family=Alex+Brush&family=Arimo:wght@400;700&family=Cinzel:wght@600&family=Cormorant+Garamond:ital,wght@1,500&family=Josefin+Sans:wght@300&family=Open+Sans:ital,wght@0,400;1,600&family=Raleway:wght@300&display=swap" rel="stylesheet">
<style>
  :root {
    --pink-soft: #f3cde4;
    --pink-mid: #e7a8cf;
    --pink-hot: #c23a75;
    --crimson: #a0153e;
    --cream: #f4f1ec;
    --paper: #ece2c8;
    --ink: #3a3a3a;
    --grey: #555;
    --rule: #c9bfa8;
  }
  * { box-sizing: border-box; margin: 0; padding: 0; }
  html, body { width: 900px; height: 1200px; overflow: hidden; }
  body { position: relative; background: var(--pink-soft); font-family: "Raleway", sans-serif; color: var(--ink); }
  .backdrop { position: absolute; inset: 0; background: radial-gradient(circle at 50% 40%, #fbe9f4, var(--pink-mid)); }
  .panel { position: absolute; inset: 0; }
  .abs { position: absolute; }

  .brand { left: 300px; top: 70px; width: 300px; height: 110px; display: flex; align-items: center; justify-content: center; gap: 10px;
    font-family: "Cinzel", serif; font-weight: 600; font-size: 26px; line-height: 1.05; color: var(--pink-hot); text-align: center; }
  .brand-dot { width: 14px; height: 14px; border-radius: 50%; background: var(--pink-hot); flex: none; }

  .nav { left: 80px; top: 232px; width: 740px; height: 32px; border-top: 2px solid #e6e2dc; border-bottom: 2px solid #e6e2dc;
    display: flex; justify-content: space-around; align-items: center; padding: 0 50px; }
  .nav a { font-family: "Cormorant Garamond", serif; font-style: italic; font-weight: 500; font-size: 19px; color: #555; text-decoration: none; }
  .nav a.current { color: var(--pink-hot); border-bottom: 1px dotted var(--pink-hot); }

  .hero-photo { left: 108px; top: 296px; width: 180px; height: 248px; border-radius: 90px 90px 6px 6px; background: linear-gradient(#8a5a3a, #5b3a24 60%, #c22a3a); }
  .hero-shadow { left: 98px; top: 545px; width: 170px; height: 30px; background: radial-gradient(ellipse at top, rgba(0,0,0,.12), transparent 70%); }

  .welcome { left: 310px; top: 316px; font-family: "Alex Brush", cursive; font-size: 29px; color: var(--pink-hot); white-space: nowrap; }
  .tagline { left: 311px; top: 350px; font-family: "Josefin Sans", sans-serif; font-weight: 300; font-size: 22px; color: var(--pink-hot); word-spacing: 10px; }
  .intro { left: 312px; top: 393px; width: 440px; font-size: 11px; line-height: 16.5px; color: var(--ink); }
  .intro p + p { margin-top: 16px; }
  .cta { left: 312px; top: 530px; width: 77px; height: 26px; background: var(--crimson); color: #fff; border: 2px solid #fff; outline: 1px solid var(--crimson);
    font-family: "Arimo", sans-serif; font-weight: 700; font-size: 9.5px; display: flex; align-items: center; justify-content: center; }

  .divider { left: 100px; width: 705px; border-top: 1px dotted var(--rule); }

  .card { top: 606px; width: 146px; height: 140px; background: var(--paper); box-shadow: 0 1px 4px rgba(0,0,0,.2); }
  .card-photo { position: absolute; left: 9px; top: 18px; width: 129px; height: 68px; }
  .card-title { position: absolute; left: 0; right: 0; top: 100px; text-align: center; font-family: "Arimo", sans-serif; font-weight: 700; font-size: 11px; line-height: 17px; color: #2d2a24; }

  .section-head { top: 795px; font-family: "Alex Brush", cursive; font-size: 28px; color: #333; }
  .post-date { font-family: "Arimo", sans-serif; font-weight: 700; font-style: italic; font-size: 10.5px; color: var(--crimson); }
  .post-text { font-family: "Arimo", sans-serif; font-size: 9px; line-height: 12.5px; color: var(--grey); margin-top: 5px; }
  .posts { left: 98px; top: 836px; width: 305px; }
  .post + .post { margin-top: 9px; padding-top: 10px; border-top: 1px solid #e0dbd2; }
  .col-rule { left: 431px; top: 808px; height: 165px; border-left: 1px solid #ddd6ca; }
  .bio { left: 459px; top: 848px; width: 335px; font-family: "Arimo", sans-serif; font-size: 9px; line-height: 12px; color: var(--grey); }
  .bio p { margin-bottom: 12px; }
  .bio strong { font-weight: 700; color: #444; }

  .footer-bar { left: 92px; top: 1005px; width: 700px; height: 36px; display: flex; align-items: center; justify-content: space-between; }
  .social { font-family: "Open Sans", sans-serif; font-weight: 600; font-size: 13px; color: #fff; background: #e01b4f; padding: 4px 7px; }
  .social.plain { background: none; color: #e01b4f; }
  .footer-link { display: flex; align-items: center; gap: 6px; font-family: "Open Sans", sans-serif; font-style: italic; font-weight: 600; font-size: 10.5px; color: #333; }
  .phone { font-family: "Open Sans", sans-serif; font-style: italic; font-weight: 600; font-size: 17px; color: #555; }
  .ornament { left: 305px; top: 1062px; width: 290px; height: 26px; background: linear-gradient(90deg, transparent, rgba(150,150,150,.35), transparent); }
  .copyright { left: 0; width: 900px; top: 1111px; text-align: center; font-family: "Open Sans", sans-serif; font-size: 8px; color: #222; }
</style>
</head>
<body>
  <div class="backdrop" role="img" aria-label="Soft pink tufted quilted satin backdrop"></div>
  <svg class="panel" width="900" height="1200" viewBox="0 0 900 1200" aria-hidden="true">
    <path d="M75,1140 L75,245 Q75,228 100,228 L250,228 Q262,228 262,205 L262,120 Q262,15 450,15 Q638,15 638,120 L638,205 Q638,228 650,228 L800,228 Q825,228 825,245 L825,1140 Q825,1150 810,1150 L90,1150 Q75,1150 75,1140 Z" fill="#f4f1ec"/>
  </svg>

  <div class="abs brand"><span class="brand-dot"></span><span>Velorim Tresses<br>Hair Designs</span></div>

  <nav class="abs nav">
    <a class="current" href="#">Home</a><a href="#">About Us</a><a href="#">Services</a><a href="#">Gallery</a><a href="#">Blog</a><a href="#">Contacts</a>
  </nav>

  <div class="abs hero-photo" role="img" aria-label="Portrait of a woman with long wavy brown hair"></div>
  <div class="abs hero-shadow"></div>

  <h1 class="abs welcome">Welcome to Velorim Tresses Hair Designs</h1>
  <div class="abs tagline">Original. Sensuous. Expressive.</div>
  <div class="abs intro">
    <p>Our salon is based on the belief that our customers' needs are of the utmost importance. Our team is committed to meeting those needs. As a result, a high percentage of our business is from repeat customers and referrals.</p>
    <p>We would welcome the opportunity to earn your trust and deliver the belief that our customers' needs are of the utmost importance. Our team is committed to meeting those needs. As a result, a high percentage of our you the best service in the industry!</p>
  </div>
  <div class="abs cta">CLICK HERE</div>

  <div class="abs divider" style="top:585px"></div>

  <div class="abs card" style="left:101px"><div class="card-photo" role="img" aria-label="Woman with long auburn hair" style="background:linear-gradient(90deg,#7a3a22,#e98a7a)"></div><div class="card-title">Terrabloom<br>Organic skincare</div></div>
  <div class="abs card" style="left:286px"><div class="card-photo" role="img" aria-label="Stylists working in the salon" style="background:linear-gradient(90deg,#8a6a4a,#d8c6a8,#6a4a3a)"></div><div class="card-title">Terrabloom<br>Organic skincare</div></div>
  <div class="abs card" style="left:470px"><div class="card-photo" role="img" aria-label="Woman relaxing during a hair treatment" style="background:linear-gradient(90deg,#3a2a30,#f2ecec 55%,#fff)"></div><div class="card-title">Terrabloom<br>Organic skincare</div></div>
  <div class="abs card" style="left:655px"><div class="card-photo" role="img" aria-label="Woman resting at a spa by the sea" style="background:linear-gradient(#6fb6e6,#d8c0b0 60%,#2a4a8a)"></div><div class="card-title">Terrabloom<br>Organic skincare</div></div>

  <h2 class="abs section-head" style="left:92px">Recent Posts</h2>
  <h2 class="abs section-head" style="left:459px">A Few Words About Me</h2>

  <div class="abs posts">
    <div class="post"><div class="post-date">January 6, 2014</div><p class="post-text">Aliquam et mauris mauris, et tempus tellus. Suspendisse placerat pretium nisi, nec pellentesque arcu vulputate at. Nulla gravida iaculis urna, eget eleifend odio malesuada non. Nulla facilisi.</p></div>
    <div class="post"><div class="post-date">December 14, 2013</div><p class="post-text">Aliquam et mauris mauris, et tempus tellus. Suspendisse placerat pretium nisi, nec pellentesque arcu vulputate at.</p></div>
  </div>
  <div class="abs col-rule"></div>
  <div class="abs bio">
    <p><strong>Certified Hair Stylist with European and Canadian experience</strong></p>
    <p>Finalist of the Lumiere 2013 - The Canadian Hairstylist of the Year Awards.</p>
    <p>Leading Stylist at fashion shows and photo shoots</p>
    <p>Trained by World Class Orvane Beauty School, Kessler Moray School (Canada), Brightlock Hair Extensions Certification (Canada), Chromalis Color School (Italy), European Hairstyle School, Varenko School (Europe)</p>
  </div>

  <div class="abs divider" style="top:993px"></div>

  <div class="abs footer-bar">
    <span class="social">Friendsy</span>
    <span class="social plain">Chatterly</span>
    <span class="footer-link"><svg width="20" height="16" viewBox="0 0 20 16"><rect x="1" y="2" width="18" height="13" fill="#e01b4f"/></svg>Get a Catalogue</span>
    <span class="footer-link"><svg width="20" height="18" viewBox="0 0 20 18"><rect x="2" y="4" width="16" height="11" fill="none" stroke="#e01b4f" stroke-width="2"/><path d="M2 4 L10 10 L18 4" fill="none" stroke="#e01b4f" stroke-width="2"/></svg>Subscribe for Newsletter</span>
    <span class="footer-link"><svg width="26" height="26" viewBox="0 0 26 26"><rect x="1" y="1" width="24" height="24" rx="4" fill="#e01b4f"/><path d="M9 6 Q7 13 12 19 L15 17 L13 14 L11 14 Q10 11 11 9 L13 9 L13 6 Z" fill="#fff"/></svg><span class="phone">012 345 0199</span></span>
  </div>

  <div class="abs ornament" role="img" aria-label="Decorative floral flourish"></div>
  <div class="abs copyright">Copyright © 2014 - Velorim Hair Studio © 2014 &nbsp;All rights reserved. Terms and Privacy Policy</div>
</body>
</html>
```